Veltrona Biz Card 2019

New business card for Veltrona Property Inspections. We are a residential home inspection company in Arizona.

Target Market(s)

Real Estate

Font styles to use
Sans Serif

Requirements
Must have
• Glen Marwick
• Home Inspector
• Veltrona Property Inspections, LLC
• 480-555-0173
• glen@veltrona-llc.example

```html
<!DOCTYPE html>
<html lang="en">
<head>
<meta charset="utf-8">
<title>Veltrona Biz Card 2019</title>
<link href="https://fonts.googleapis.com/css2?family=Lato:wght@400;700;900&display=swap" rel="stylesheet">
<style>
  :root {
    --backdrop: #d6d6d6;
    --card: #2a2a2a;
    --green: #45b649;
    --light: #ececec;
    --rule: #555555;
  }
  html, body {
    margin: 0;
    width: 1200px;
    height: 1200px;
    overflow: hidden;
    background: var(--backdrop);
    font-family: "Lato", sans-serif;
  }
  .canvas { position: relative; width: 1200px; height: 1200px; }
  .card {
    position: absolute;
    left: 250px;
    width: 708px;
    height: 404px;
    background: var(--card);
  }
  .card--front { top: 144px; }
  .card--back { top: 582px; }

  .brand {
    position: absolute;
    display: flex;
    align-items: center;
    gap: 14px;
    color: var(--light);
    font-weight: 900;
    letter-spacing: 2px;
    text-transform: uppercase;
    line-height: 1;
  }
  .brand__square {
    width: 0.62em;
    height: 0.62em;
    background: var(--green);
  }
  .card--front .brand {
    left: 0; right: 0;
    top: 178px;
    justify-content: center;
    font-size: 46px;
  }
  .card--back .brand {
    left: 86px;
    top: 184px;
    font-size: 32px;
  }

  .divider {
    position: absolute;
    left: 354px;
    top: 132px;
    width: 1px;
    height: 130px;
    background: var(--rule);
  }
  .details {
    position: absolute;
    left: 374px;
    top: 100px;
    color: var(--light);
    font-size: 16.5px;
    line-height: 1.45;
  }
  .details p { margin: 0; }
  .details__name { color: var(--green); font-weight: 700; font-size: 22px; line-height: 1.2; }
  .details__company { color: var(--green); margin-top: 14px !important; }
  .details__contact { margin-top: 14px !important; }
  .details__line { display: flex; align-items: center; gap: 8px; }
  .details__line svg { width: 12px; height: 12px; fill: var(--green); }
</style>
</head>
<body>
<main class="canvas">
  <section class="card card--front" aria-label="Card front">
    <div class="brand"><span class="brand__square"></span>Veltrona</div>
  </section>

  <section class="card card--back" aria-label="Card back">
    <div class="brand"><span class="brand__square"></span>Veltrona</div>
    <div class="divider"></div>
    <div class="details">
      <p class="details__name">Glen Marwick</p>
      <p>Home Inspector</p>
      <p class="details__company">Veltrona Property Inspections, LLC</p>
      <p>4410 S. Harlow Ave.</p>
      <p>Tempe, AZ 85283</p>
      <div class="details__contact">
        <p class="details__line">
          <svg viewBox="0 0 24 24" aria-hidden="true"><path d="M6.6 10.8a15.1 15.1 0 0 0 6.6 6.6l2.2-2.2c.3-.3.7-.4 1-.2 1.1.4 2.3.6 3.6.6.6 0 1 .4 1 1V20c0 .6-.4 1-1 1A17 17 0 0 1 3 4c0-.6.4-1 1-1h3.5c.6 0 1 .4 1 1 0 1.3.2 2.5.6 3.6.1.3 0 .7-.2 1z"/></svg>
          480-555-0173
        </p>
        <p class="details__line">
          <svg viewBox="0 0 24 24" aria-hidden="true"><path d="M2 5h20v14H2z M2 5l10 8 10-8" /></svg>
          glen@veltrona-llc.example
        </p>
      </div>
    </div>
  </section>
</main>
</body>
</html>
```